Japanese Rice Food Package Label

- We are launching Japanese food products to the outdoor community.
- Made in Japan
- We will have multiple flavors of rice but want to keep the package label almost the same and only replace the flavor text (e.g., Mixed Rice, Curry Rice, etc)
- We like simple designs inspired by Japan.
- Label size: 105 mm x148 mm
- Our brand: YURATO https://yurato.co/
- Video message: https://www.clipvane.com/share/4b7e19d0a3c65f2e8d1a7b30c9e5f412

```html
<!DOCTYPE html>
<html lang="en">
<head>
<meta charset="utf-8">
<title>YURATO Mixed Rice Label</title>
<link rel="stylesheet" href="https://fonts.googleapis.com/css2?family=Archivo+Black&family=Inter:wght@400&family=Rubik:ital,wght@1,800&display=swap">
<style>
  :root {
    --page: #efefed;
    --label: #ffffff;
    --frame: #d6d6d6;
    --ink: #111111;
    --red: #e3192f;
    --mist: #f2f2f2;
  }
  * { margin: 0; padding: 0; box-sizing: border-box; }
  html, body { width: 1200px; height: 682px; overflow: hidden; background: var(--page); }
  .label {
    position: absolute; left: 148px; top: 21px;
    width: 904px; height: 640px;
    background: var(--label);
    border: 2px solid var(--frame);
    overflow: hidden;
  }
  .sun {
    position: absolute; left: 120px; top: 62px;
    width: 450px; height: 450px; border-radius: 50%;
    background: var(--mist);
  }
  .samurai-art {
    position: absolute; left: 70px; top: 40px;
    width: 590px; height: 300px;
    background: linear-gradient(160deg, rgba(227,25,47,0.00) 10%, rgba(227,25,47,0.07) 55%, rgba(227,25,47,0.12) 100%);
  }
  .product-kind {
    position: absolute; left: 61px; top: 358px;
    font: 400 31px/1 "Inter", sans-serif; color: var(--ink);
    letter-spacing: -0.2px;
  }
  .flavor {
    position: absolute; left: 58px; top: 396px;
    font: 400 72px/1 "Inter", sans-serif; color: var(--ink);
    letter-spacing: -1px;
  }
  .badges {
    position: absolute; left: 59px; top: 494px;
    display: flex; gap: 20px;
  }
  .badge { width: 96px; height: 96px; display: block; }
  .brand {
    position: absolute; left: 728px; top: 58px;
    width: 145px; height: 552px;
  }
  .brand text { font-family: "Archivo Black", sans-serif; fill: var(--ink); }
  .long-life { font-family: "Rubik", sans-serif; font-style: italic; font-weight: 800; }
  .timer-text { font-family: "Inter", sans-serif; }
</style>
</head>
<body>
  <main class="label">
    <div class="sun"></div>
    <div class="samurai-art" role="img" aria-label="Red line illustration of a samurai hand drawing a katana"></div>

    <p class="product-kind">Dried Rice Food</p>
    <h1 class="flavor">Mixed Rice</h1>

    <div class="badges">
      <svg class="badge" viewBox="0 0 96 96" role="img" aria-label="No cooking pot needed">
        <circle cx="48" cy="48" r="43" fill="#fff" stroke="var(--red)" stroke-width="7"/>
        <rect x="24" y="44" width="48" height="28" rx="4" fill="var(--ink)"/>
        <rect x="18" y="40" width="60" height="6" rx="3" fill="var(--ink)"/>
        <circle cx="48" cy="35" r="4" fill="var(--ink)"/>
        <line x1="19" y1="19" x2="77" y2="77" stroke="var(--red)" stroke-width="7"/>
      </svg>
      <svg class="badge" viewBox="0 0 96 96" role="img" aria-label="Just add water">
        <circle cx="48" cy="48" r="48" fill="var(--ink)"/>
        <path d="M40 30 L72 40 L52 66 Z" fill="none" stroke="var(--red)" stroke-width="4" stroke-linejoin="round"/>
        <path d="M40 30 Q34 22 42 20 Q50 20 48 28" fill="none" stroke="var(--red)" stroke-width="3"/>
        <path d="M38 44 Q24 58 16 70" fill="none" stroke="var(--red)" stroke-width="3"/>
      </svg>
      <svg class="badge" viewBox="0 0 96 96" role="img" aria-label="Ready in 15 minutes">
        <circle cx="48" cy="48" r="48" fill="var(--ink)"/>
        <path d="M22 54 A27 27 0 1 0 48 21" fill="none" stroke="var(--red)" stroke-width="4"/>
        <path d="M16 54 L22 44 L28 54 Z" fill="var(--red)"/>
        <text class="timer-text" x="48" y="46" text-anchor="middle" font-size="26" fill="var(--red)">15</text>
        <text class="timer-text" x="48" y="68" text-anchor="middle" font-size="17" fill="var(--red)">min</text>
      </svg>
      <svg class="badge" viewBox="0 0 96 96" role="img" aria-label="Long life">
        <circle cx="48" cy="48" r="48" fill="var(--ink)"/>
        <text class="long-life" x="48" y="44" text-anchor="middle" font-size="21" fill="var(--red)">Long</text>
        <text class="long-life" x="48" y="67" text-anchor="middle" font-size="21" fill="var(--red)">Life</text>
      </svg>
    </div>

    <svg class="brand" viewBox="0 0 145 552" aria-label="YURATO">
      <text transform="translate(140 550) rotate(-90)" font-size="190" textLength="548" lengthAdjust="spacingAndGlyphs">YURATO</text>
    </svg>
  </main>
</body>
</html>
```